Skin cancer clinic services trifold brochure

Need trifold brochure listing skin cancer services our clinic provides, staff information, location and brief about skin cancer with colours similar to our web site www.Dermavoy.clinic. I will provide more information regarding services and staff but want this colourful and standout as it will be given to other referring doctors or patients
Updates

Target Market(s)

Age 40 to 80 years

Industry/Entity Type

Medical

Font styles to use
Serif

Colors

Designer to choose colors to be used in the design.

Requirements
Must have
• Logo, services, contact info, beach or sun look and colours similar to web site or logo

```html
<!DOCTYPE html>
<html lang="en">
<head>
<meta charset="utf-8">
<title>Dermavoy Skin Cancer Clinic – Trifold Brochure</title>
<link rel="stylesheet" href="https://fonts.googleapis.com/css2?family=Marcellus&family=Montserrat:ital,wght@0,400;0,600;0,700;1,400&display=swap">
<style>
:root{
  --bg:#dcdcdc;
  --paper:#ffffff;
  --paper-shade:#f1f1f1;
  --ink:#2b2b2b;
  --ink-soft:#555;
  --blue:#2f8fd6;
  --orange:#f29a1f;
  --orange-deep:#ec8318;
  --yellow:#f8d54a;
  --gold:#f3b33a;
}
*{box-sizing:border-box;margin:0;padding:0}
html,body{width:960px;height:1200px;overflow:hidden;background:var(--bg)}
body{font-family:"Montserrat",Arial,sans-serif;color:var(--ink);position:relative}

.spread{position:absolute;left:30px;width:900px;height:560px;background:var(--paper);display:flex;box-shadow:0 6px 18px rgba(0,0,0,.18);overflow:hidden}
.spread--outside{top:30px}
.spread--inside{top:610px}
.panel{position:relative;width:300px;height:100%;padding:26px 24px;z-index:2}
.panel + .panel{border-left:1px solid rgba(0,0,0,.05)}
.decor{position:absolute;inset:0;z-index:1}

.heading{font-weight:700;font-size:11px;letter-spacing:.5px;color:var(--blue);text-transform:uppercase;margin-bottom:8px}
.heading--large{font-size:15px;text-transform:none;font-weight:600;letter-spacing:.3px}
.body{font-size:7.4px;line-height:1.55;color:var(--ink-soft)}
.body em{font-style:italic}
.tagline{font-size:10px;font-weight:600;color:var(--ink);margin:16px 0 2px}
.welcome{font-size:8px;line-height:1.5;color:var(--ink)}
.welcome strong{font-weight:700}

.staff{list-style:none;margin:8px 0 14px}
.staff li{position:relative;padding-left:12px;margin-bottom:7px}
.staff li::before,.services li::before{content:"";position:absolute;left:0;top:3px;width:4px;height:4px;border-radius:50%;background:var(--orange)}
.staff .name{display:block;font-size:8.6px;font-weight:700;color:var(--ink)}
.staff .quals{display:block;font-size:6.8px;color:var(--ink-soft);line-height:1.4}

.panel--contact{text-align:center;padding-top:60px}
.map{width:120px;height:120px;border-radius:50%;margin:0 auto 8px;background:radial-gradient(circle at 55% 45%,#f4f1ea,#dfe7ee 70%,#cfe0ec);border:2px solid #bcd3e6}
.rating{font-size:7px;color:var(--orange);letter-spacing:1px;margin-bottom:4px}
.rating b{color:var(--ink-soft);font-weight:600;margin-right:3px}
.address{font-size:9px;line-height:1.45;color:var(--ink);margin-bottom:28px}
.contact-list{font-size:10px;line-height:1.65;color:var(--ink)}
.contact-list strong{font-weight:700}
.contact-foot{display:flex;align-items:flex-end;justify-content:center;gap:34px;margin-top:30px}
.badge{width:30px;height:30px;background:#3a3f9a}
.follow{font-size:6px;font-weight:700;color:var(--orange);letter-spacing:.6px;text-transform:uppercase}
.follow .dots{display:flex;gap:7px;justify-content:center;margin-top:5px}
.follow .dots span{width:14px;height:14px;border-radius:50%;background:var(--orange)}

.brand{position:absolute;left:36px;bottom:62px;display:flex;align-items:center;gap:10px}
.brand__mark{width:22px;height:22px;border-radius:50%;background:var(--orange)}
.brand__name{font-family:"Marcellus",Georgia,serif;font-size:32px;color:var(--ink);letter-spacing:1px}
.brand__tag{position:absolute;left:68px;bottom:46px;font-family:"Marcellus",Georgia,serif;font-size:10px;letter-spacing:2px;color:var(--ink);text-transform:uppercase}

.title{font-family:"Marcellus",Georgia,serif;font-size:36px;color:var(--ink);margin:4px 0 14px}
.did-you-know{font-size:11px;font-weight:700;color:var(--blue);text-transform:uppercase;margin-bottom:6px}
.intro{font-size:8.2px;line-height:1.6;color:var(--ink)}
.intro p + p{margin-top:6px}
.photo{position:absolute;left:60px;top:290px;width:190px;height:150px;border-radius:50%;background:radial-gradient(circle at 50% 40%,#e9c7a8,#9fc7d8 75%);}

.services{list-style:none;margin-top:6px}
.services li{position:relative;padding-left:10px;font-size:7px;line-height:1.5;color:var(--ink-soft);margin-bottom:7px}
.services li strong{color:var(--ink);font-weight:700}
.services a{color:var(--blue);text-decoration:none}
</style>
</head>
<body>

<!-- Outside spread -->
<section class="spread spread--outside">
  <svg class="decor" viewBox="0 0 900 560" preserveAspectRatio="none" aria-hidden="true">
    <defs>
      <linearGradient id="sun-out" x1="0" y1="0" x2="1" y2="1">
        <stop offset="0" stop-color="#f6c843"/>
        <stop offset=".55" stop-color="#f29a1f"/>
        <stop offset="1" stop-color="#f0a42a"/>
      </linearGradient>
    </defs>
    <path d="M470 0 C600 0 640 110 640 250 C640 380 850 420 900 560 L900 0 Z" fill="#2f8fd6"/>
    <path d="M486 0 C612 0 650 110 650 250 C650 372 860 410 900 540 L900 0 Z" fill="url(#sun-out)"/>
  </svg>

  <div class="panel panel--about">
    <h2 class="heading">About Us</h2>
    <p class="body"><em>Dermavoy Skin Cancer Clinic is a purpose-built skin cancer clinic dedicated to providing the highest-level patient care to the Central Coast community and surrounding regions. Our skilled doctors and nurses have extensive experience and advanced training in Skin Cancer Medicine in order to provide quality care to our patients. We specialise in a comprehensive approach to skin with preventive skin cancer care, expert diagnostic dermoscopy skills highlighting artificial intelligent analytics, and definitive surgical and medical treatments of skin cancers.</em></p>
    <p class="tagline">Skin cancer medicine is all we do.</p>
    <p class="welcome">We welcome you to "virtually" walk through our clinic at <strong>www.Dermavoy.clinic</strong></p>

    <h2 class="heading" style="margin-top:14px">Our Staff</h2>
    <p class="body"><em>At Dermavoy Skin Cancer Clinic, our highly qualified administrative staff, nurses and doctors are an integral part of the team ensuring excellent clinical care is provided to our patients. We currently have 5 experienced local doctors.</em></p>
    <ul class="staff">
      <li><span class="name">Dr. Clara Whitfield</span><span class="quals">BMed, FRACGP, Diploma Skin Cancer Medicine/Surgery, Diploma Aesthetic Medicine</span></li>
      <li><span class="name">Dr. Maya Renshaw</span><span class="quals">BMed, FRACGP, Diploma Skin Cancer Medicine/Surgery</span></li>
      <li><span class="name">Dr. Elise Hartnell</span><span class="quals">MBBS, FRACGP</span></li>
      <li><span class="name">Dr. Owen Castell</span><span class="quals">MBBS (Syd), Dip Law</span></li>
      <li><span class="name">Dr. Nora Aldgate</span><span class="quals">MBBS (Hons), FRACGP, Cert. Skin Cancer Medicine</span></li>
    </ul>
    <p class="body"><em>Early detection of skin cancers is vital for the best outcome. Dermavoy has invested in technology and research to provide the latest diagnostic services and treatments to meet the needs of our patients.</em></p>
  </div>

  <div class="panel panel--contact">
    <div class="map" role="img" aria-label="Street map showing the clinic location"></div>
    <p class="rating"><b>5.0</b>★★★★★</p>
    <p class="address">Suite 4, 210 Harbour Road<br>Seabrook, NSW 2999</p>
    <h2 class="heading heading--large">CONTACT US NOW</h2>
    <p class="contact-list">
      Phone: <strong>1300 55 0190</strong><br>
      Email: admin@Dermavoy.clinic<br>
      Web site: www.Dermavoy.clinic<br>
      Fax: 4300 0182
    </p>
    <div class="contact-foot">
      <div class="badge" role="img" aria-label="Accreditation badge"></div>
      <div class="follow">Follow us on
        <div class="dots"><span></span><span></span><span></span></div>
      </div>
    </div>
  </div>

  <div class="panel panel--cover">
    <div class="brand">
      <span class="brand__mark"></span>
      <span class="brand__name">DERMAVOY</span>
    </div>
    <p class="brand__tag">Skin Cancer Clinic</p>
  </div>
</section>

<!-- Inside spread -->
<section class="spread spread--inside">
  <svg class="decor" viewBox="0 0 900 560" preserveAspectRatio="none" aria-hidden="true">
    <defs>
      <linearGradient id="sun-in" x1="0" y1="0" x2="1" y2="1">
        <stop offset="0" stop-color="#f8d54a"/>
        <stop offset=".6" stop-color="#f29a1f"/>
        <stop offset="1" stop-color="#ec8318"/>
      </linearGradient>
    </defs>
    <path d="M0 400 C70 455 150 478 260 478 C380 478 470 470 560 480 C600 500 610 540 620 560 L0 560 Z" fill="#2f8fd6"/>
    <path d="M0 412 C70 465 150 488 260 488 C380 488 470 480 556 490 C592 508 600 540 606 560 L0 560 Z" fill="url(#sun-in)"/>
  </svg>

  <div class="panel panel--intro">
    <h1 class="title">Skin Cancer</h1>
    <h2 class="did-you-know">Did you know?</h2>
    <div class="intro">
      <p>Skin Cancers account for 80% of all newly diagnosed cancers with two in three Australians diagnosed with skin cancer by the time they are 70. Although over 90% of skin cancers are due to over exposure to UV light, some are caused by chemical exposure or are hereditary. Over 2000 Australians die from skin cancer each year.</p>
      <p>Have you had your skin checked lately?</p>
    </div>
    <div class="photo" role="img" aria-label="Photo of a smiling senior couple embracing"></div>
  </div>

  <div class="panel panel--services">
    <h2 class="heading heading--large">Professional Skin Services</h2>
    <ul class="services">
      <li><strong>Advanced Skin Cancer Detection</strong> with detailed Full Body skin checks using dermoscopy and technology to minimise unnecessary excisions.</li>
      <li><strong>Individual Mole mapping and full body photography</strong> utilising intelligent skin analytics with SkinTrace – an artificial intelligence-powered platform which provides tools for documenting and diagnosing skin cancers and evidence-based care.</li>
      <li><strong>MoleView Skin Imaging System</strong> which captures high-quality images using SpectraScan – clinically proven technology which provides a unique level of detail up to 2mm beneath the skin's surface.</li>
      <li><strong>Purpose Built Skin Cancer Facility</strong> providing Surgical treatments in 2 dedicated fully equipped theatres and Treatment room staffed by skilled skin cancer medicine nurses.</li>
      <li><strong>Large referral basis</strong> for our patients that may require extensive therapy for their skin cancers, including Radiotherapy for cosmetically sensitive areas, or care under the Coastal Melanoma Centre.</li>
      <li><strong>Priority Spot Checks</strong> – appointments are set aside every day for urgent suspicious lesions allowing for quick evaluation, whether for an existing or new patient.</li>
      <li><strong>GP Team Approach</strong> – Dermavoy believes an integrated team approach to a patient's skin cancer care is important, and findings are shared with their GP upon permission.</li>
      <li><strong>Pain minimisation Techniques</strong> – Topical numbing creams and cooling agents are available to minimise tenderness. Our theatres play calming nature scenes to ensure our patients are comfortable.</li>
    </ul>
  </div>

  <div class="panel panel--treatments">
    <h2 class="heading heading--large">Specialised Treatments</h2>
    <ul class="services">
      <li><strong>Surgical Procedures</strong> – Our Doctors are proficient in surgical procedures from simple diagnostic biopsies or elliptical excisions to advanced procedures including skin grafts and surgical flap repair, all under a local anaesthetic.</li>
      <li><strong>RadioLite Radiofrequency procedures</strong> – Surgical options include a high frequency radiosurgical device for scalpel-less surgery. It allows our Doctors to use radiowaves instead of scalpels to provide advanced skin cancer surgical procedures or cosmetic procedures, including removal of spider veins, skin tags, seborrheic keratoses, warts and other raised lesions, with minimal thermal damage, bleeding and recovery time.</li>
      <li><strong>Margin Controlled Surgery</strong> (also known as Slow Mohs or Delayed Closure) – a process where aggressive skin cancers are not closed after excision until the histological status and clearance is known. This can minimise the need for larger excisions and give a better cosmetic outcome, especially in sensitive regions such as the nose, ears and face.</li>
      <li><strong>Non-surgical treatments and preventative therapy options</strong> – Our goal is to prevent and treat skin cancer in the least invasive way possible. This includes preventative care including vitamin B3 benefits and sun safe practices, topical therapies, liquid nitrogen and prescriptive therapy for solar keratoses.</li>
      <li><strong>Cosmetic Services</strong> – Dermavoy approaches our skin cancer patient holistically and, by appointment, we can offer advice and treatment regarding skin pigmentation, troublesome bumps and lumps and more! Please see our web site at <a>www.Dermavoy.clinic</a> for more information.</li>
    </ul>
  </div>
</section>

</body>
</html>
```